Website for New Phone Company

Our company "Lagoonway Telecom" requires a new web-site.

We enable Pacific Islanders (Fijians, Samoans, Tongans) to speak to their friends and family back home for a fraction of the cost of other phone companies whilst maintaining a quality. Our target audience is price sensitive but is demanding with quality, we would like them to gather a feel that they are dealing with a safe company that is orientated towards the Pacific Island community, has low pricing and yet doesn't compromise on quality.

We are going to be marketing via online channels and so a Google friendly web-site is important. We essentially need three pages designed which we will use with our content.

Page 1 - Homepage Lagoonway Telecom - Our prime brand is Lagoonway Telecom and we would like to promote this brand on our web-site.

However, we have three plans under this brand called Verelo, Makiri and Nemali. We would like the main page to have three unique service offerings for Nemali, Makiri and Verelo. Something along the lines of being able to choose a plan down on the page. I would like to give examples here of companies in our industry that are extremely successful in this trade i.e. www.dialquay.co.nz, www.9speak.co.nz, www.telvira.com

The objective of this design is to present the customer with three unique offerings targeted to Samoa (Nemali), Makiri (Tonga) and Verelo (Fiji).

Page 2 - Content/Template Page for Lagoonway Telecom - We require a page where we can place content like About Us, Contact Us etc.

Page 3 - We require a single design that will fit all three brands as per the brand images attached for Verelo, Nemali and Makiri. This will almost be used as a landing page to brand the plan exclusively under our company. All three plans / service offerings are being marketed under "Lagoonway Telecom" which makes it important to use both the service offering logo as well as the company logo. This page needs to act more as a promotional page where it promotes our service offering. e.g. Call Samoa from only 50c a minute type of thing.

The objective of the design of the landing / service offering page is to entice the customer to act upon the offer by joining our organisation.

We will be available throughout the process to guide you better.
Updates

Project Deadline Extended
Reason: We haven't received suitable designs to choose from. We would like to see quality work not quantity.

Industry/Entity Type

It Company

```html
<!DOCTYPE html>
<html lang="en">
<head>
<meta charset="utf-8">
<title>Lagoonway Telecom</title>
<link rel="stylesheet" href="https://fonts.googleapis.com/css2?family=Oswald:wght@400;500&family=Merriweather:wght@400;700&family=Open+Sans:wght@400;600;700&display=swap">
<style>
:root{
  --red:#d62a1e;
  --red-deep:#c7221a;
  --ink:#333;
  --muted:#7a7a7a;
  --paper:#f0f0f0;
  --card-text:#f6f6f6;
  --makiri:#0e5a37;
  --nemali:#1f5fa9;
  --verelo:#a8442b;
  --client:#5a5a5a;
  --footer:#1e1e1e;
  --footer-low:#161616;
  --footer-line:#333;
  --footer-text:#9a9a9a;
}
*{box-sizing:border-box;margin:0;padding:0}
html,body{width:1200px;height:2476px;overflow:hidden}
body{font-family:"Open Sans",Arial,sans-serif;color:var(--ink);background:var(--paper);position:relative}

.site-header{position:absolute;top:0;left:0;width:1200px;height:64px;background:var(--red);display:flex;align-items:center;justify-content:space-between;padding:0 56px}
.brand{display:flex;align-items:center;gap:12px;color:#fff}
.brand-dot{width:40px;height:40px;border-radius:50%;background:#fff}
.brand-name{font-weight:700;font-size:26px;line-height:1}
.brand-name small{display:block;font-size:14px;font-weight:700;margin-top:3px}
.main-nav{display:flex;gap:30px}
.main-nav a{color:#fff;text-decoration:none;font-size:13px;font-weight:600;letter-spacing:.5px;text-transform:uppercase}
.main-nav a.has-menu::after{content:"";display:inline-block;margin-left:6px;border:4px solid transparent;border-top-color:#fff;vertical-align:-2px}

.hero{position:absolute;top:64px;left:0;width:1200px;height:568px;
  background:
    radial-gradient(ellipse 260px 170px at 790px 390px,#2b2b2e 0%,#3d3c3e 55%,rgba(60,58,58,0) 100%),
    radial-gradient(ellipse 520px 260px at 300px 470px,#a8754a 0%,rgba(150,100,60,.55) 55%,rgba(150,100,60,0) 100%),
    linear-gradient(180deg,#d9dcdc 0%,#c7c3bc 45%,#b49a80 100%)}

.welcome{position:absolute;top:632px;left:0;width:1200px;height:280px;background:var(--red-deep);display:flex;align-items:center;justify-content:center}
.welcome p{width:960px;text-align:center;font-family:"Merriweather",Georgia,serif;font-size:20px;line-height:1.55;color:#fff}
.welcome strong{font-weight:700;color:#ffe9c9}
.scroll-cue{position:absolute;left:572px;top:884px;width:56px;height:56px;border-radius:50%;background:#fff}

.section-title{position:absolute;left:0;width:1200px;text-align:center;font-family:"Oswald",Arial,sans-serif;font-size:28px;font-weight:500;letter-spacing:1px}
.section-title::after{content:"";display:block;width:972px;height:1px;background:#d3d3d3;margin:8px auto 0}
.services-title{top:962px;color:var(--red)}
.clients-title{top:1548px;color:#3a3a4a}

.plans{position:absolute;top:1032px;left:112px;width:972px;display:flex;justify-content:space-between}
.plan{width:316px;height:468px;background:var(--card-text)}
.plan-mark{height:212px;display:flex;align-items:center;justify-content:center;gap:12px;color:#fff;font-weight:700;font-size:34px}
.plan-mark .dot{width:26px;height:26px;border-radius:50%;background:#fff}
.plan--makiri .plan-mark{background:var(--makiri)}
.plan--nemali .plan-mark{background:var(--nemali)}
.plan--verelo .plan-mark{background:var(--verelo)}
.plan h3{margin-top:22px;text-align:center;font-family:"Oswald",Arial,sans-serif;font-weight:500;font-size:17px;color:var(--red)}
.plan p{margin:8px auto 0;width:236px;text-align:center;font-family:"Merriweather",Georgia,serif;font-size:12.5px;line-height:1.7;color:var(--muted)}
.plan--makiri{border-bottom:4px solid var(--red)}

.clients-intro{position:absolute;top:1614px;left:112px;width:972px;text-align:center;font-family:"Merriweather",Georgia,serif;font-size:19px;line-height:1.6;color:#8a8a8a}
.client-row{position:absolute;top:1740px;left:112px;width:972px;height:140px;display:flex;justify-content:space-around;align-items:center}
.client{display:flex;align-items:center;gap:10px;font-weight:700;font-size:24px;color:var(--client)}
.client-dot{width:14px;height:14px;border-radius:50%;background:var(--client)}

.site-footer{position:absolute;top:1960px;left:0;width:1200px;height:516px;background:var(--footer);color:var(--footer-text)}
.newsletter{position:absolute;top:40px;left:112px;width:972px;height:48px;display:flex;align-items:center}
.newsletter h4{font-size:13px;font-weight:700;color:#fff;letter-spacing:.5px;white-space:nowrap}
.newsletter .rule{flex:1;height:1px;background:var(--footer-line);margin:0 24px}
.newsletter .field{width:300px;height:44px;background:#2c2c2c;border:1px solid #3a3a3a;color:#777;font-size:12px;font-style:italic;display:flex;align-items:center;padding-left:16px}
.newsletter .btn{width:224px;height:44px;margin-left:28px;background:var(--red);color:#fff;font-size:13px;font-weight:700;display:flex;align-items:center;justify-content:center;letter-spacing:.5px}
.footer-nav{position:absolute;top:146px;left:112px;display:flex;gap:32px}
.footer-nav a{color:#fff;text-decoration:none;font-size:12px;font-weight:700;letter-spacing:.5px}
.footer-divider{position:absolute;top:204px;left:112px;width:972px;height:1px;background:var(--footer-line)}
.footer-col{position:absolute;top:256px;width:420px}
.footer-col h4{color:#fff;font-size:13px;font-weight:700;letter-spacing:.5px;margin-bottom:14px}
.footer-col p{font-size:12px;line-height:1.8}
.about{left:112px}
.contact{left:612px}
.footer-base{position:absolute;bottom:0;left:0;width:1200px;height:76px;background:var(--footer-low);display:flex;align-items:center;justify-content:space-between;padding:0 112px;font-size:12px}
.social{display:flex;gap:22px;color:#ccc}
.social span{display:flex;align-items:center;gap:6px}
.social i{display:inline-block;width:8px;height:8px;background:#ccc}
</style>
</head>
<body>

<header class="site-header">
  <div class="brand">
    <span class="brand-dot"></span>
    <span class="brand-name">Lagoonway<small>Telecom</small></span>
  </div>
  <nav class="main-nav">
    <a href="#">Home</a>
    <a href="#" class="has-menu">Services</a>
    <a href="#" class="has-menu">Products</a>
    <a href="#">Contact</a>
  </nav>
</header>

<div class="hero" role="img" aria-label="Photo of a person relaxing at home on a wooden floor, holding a tablet, with a cup of coffee and a coffee press beside them"></div>

<section class="welcome">
  <p><strong>Welcome</strong> We lets you make U.S. and international calls using your high-speed Internet connection (VoIP) and helps you save money every month with great calling plans. You can choose international and domestic plans that include unlimited calling plus a full range of features. All for a price that's hard to beat.</p>
</section>
<svg class="scroll-cue" viewBox="0 0 56 56" aria-hidden="true"><polyline points="19,24 28,33 37,24" fill="none" stroke="#d62a1e" stroke-width="3" stroke-linecap="round" stroke-linejoin="round"/></svg>

<h2 class="section-title services-title">SERVICES</h2>
<div class="plans">
  <article class="plan plan--makiri">
    <div class="plan-mark"><span class="dot"></span>Makiri</div>
    <h3>Makiri</h3>
    <p>Lorem ipsum dolor sit amet, consectetur adipisicing elit, sed do eiusmod tempor incididunt ut labore et dolore magna aliqua. Ut enim ad minim veniam, quis nostrud exercitation ullamco.</p>
  </article>
  <article class="plan plan--nemali">
    <div class="plan-mark"><span class="dot"></span>Nemali</div>
    <h3>Nemali</h3>
    <p>Sed ut perspiciatis unde omnis iste natus error sit voluptatem accusantium doloremque laudantium, totam rem aperiam, eaque ipsa quae ab illo inventore veritatis et quasi architecto.</p>
  </article>
  <article class="plan plan--verelo">
    <div class="plan-mark"><span class="dot"></span>Verelo</div>
    <h3>Verelo</h3>
    <p>At vero eos et accusamus et iusto odio dignissimos ducimus qui blanditiis praesentium voluptatum deleniti atque corrupti quos dolores et quas molestias excepturi sint occaecati.</p>
  </article>
</div>

<h2 class="section-title clients-title">OUR CLIENTS</h2>
<p class="clients-intro">Sed ut perspiciatis unde omnis iste natus error sit voluptatem accusantium doloremque laudantium, totam rem aperiam, eaque ipsa quae ab illo inventore veritatis et quasi architecto beatae vitae dicta sunt explicabo.</p>
<div class="client-row">
  <span class="client">Heritage Cycles</span>
  <span class="client">Spoke &amp; Co.</span>
  <span class="client">Prairie Wheels</span>
  <span class="client"><span class="client-dot"></span>Summit Riders</span>
</div>

<footer class="site-footer">
  <div class="newsletter">
    <h4>GET OUR NEWSLETTER</h4>
    <span class="rule"></span>
    <div class="field">Enter your email</div>
    <div class="btn">SIGN UP</div>
  </div>
  <nav class="footer-nav">
    <a href="#">FRONTPAGE</a>
    <a href="#">FEATURES</a>
    <a href="#">PAGES</a>
    <a href="#">BLOG</a>
  </nav>
  <div class="footer-divider"></div>
  <div class="footer-col about">
    <h4>ABOUT US</h4>
    <p>Lorem ipsum dolor sit amet, consectetur adipiscing elit, sed do eiusmod tempor incididunt ut labore et dolore magna aliqua. Ut enim ad minim veniam, quis nostrud exercitation ullamco laboris nisi ut aliquip ex ea commodo consequat.</p>
  </div>
  <div class="footer-col contact">
    <h4>CONTACT US</h4>
    <p>Postbox 12 Lagoon Road, Auckland 1010<br>Phone: (09) 555 0142<br>Email: hello@lagoonway.co.nz<br>Web: www.lagoonway.co.nz</p>
  </div>
  <div class="footer-base">
    <span>© 2014 Lagoonway Telecom. All rights reserved.</span>
    <div class="social">
      <span><i></i>Flitter</span>
      <span><i></i>Friendbook</span>
      <span><i></i>Globeplus</span>
    </div>
  </div>
</footer>

</body>
</html>
```